Diagnostic MRI imaging center needs a website

We need a website design for a new diagnositic MRI imaging center.
Please refer to the attachment of guideline.

Coding

Coded - Design and coding required

Number of Pages Required

5+ page

Requirements
Must have
• Corvane Helixa MRI scanner images, NOT CT scanner images. Thanks
Nice to have
• Please only show MRI scanner images, not CT and other modalities
Should not have
• CT and other modalities scanner images

```html
<!DOCTYPE html>
<html lang="en">
<head>
<meta charset="utf-8">
<title>Diagnostic MRI Imaging Center</title>
<link href="https://fonts.googleapis.com/css2?family=Poppins:ital,wght@0,400;0,500;0,600;0,700;1,400&family=Roboto+Slab:wght@700;800&display=swap" rel="stylesheet">
<style>
:root{
  --teal:#1f7f75;
  --teal-dark:#16655d;
  --teal-light:#dcf1f2;
  --ink:#111111;
  --text:#555555;
  --white:#ffffff;
  --footer:#171717;
  --star:#f26a1b;
  --photo-a:#6f8f98;
  --photo-b:#b9cdd3;
}
*{margin:0;padding:0;box-sizing:border-box}
html,body{width:1200px;height:4651px;overflow:hidden}
body{font-family:'Poppins',sans-serif;color:var(--ink);background:var(--white);position:relative}
.slab{font-family:'Roboto Slab',serif;font-weight:800;letter-spacing:.5px}
.teal{color:var(--teal)}
section,header,footer{position:absolute;left:0;width:1200px}
.abs{position:absolute}
.btn{position:absolute;display:flex;align-items:center;justify-content:center;border-radius:22px;background:var(--teal);color:var(--white);font-size:14px;font-weight:500;white-space:nowrap}
.photo{position:absolute;background:linear-gradient(135deg,var(--photo-a),var(--photo-b))}
p.body{font-size:14px;line-height:27px;color:var(--text)}

/* top bar */
.topbar{top:0;height:36px;background:var(--ink);color:#eee;font-size:13px;display:flex;justify-content:center;align-items:center;gap:44px}
.topbar span{display:flex;align-items:center;gap:7px}

/* hero */
.hero{top:36px;height:686px;overflow:hidden}
.hero-photo{position:absolute;inset:0;background:linear-gradient(120deg,#2f4f57 0%,#7d99a3 35%,#c7d6da 60%,#9fb6bc 100%)}
.hero-shade{position:absolute;inset:0;background:linear-gradient(90deg,rgba(10,35,40,.55),rgba(10,35,40,0) 55%)}
.hero-curve{position:absolute;left:0;top:0}
.nav{position:absolute;top:22px;left:0;width:1200px;height:40px}
.logo{position:absolute;left:100px;top:6px;font-size:28px;font-weight:600;color:var(--white)}
.menu{position:absolute;left:395px;top:12px;display:flex;gap:32px;font-size:14px;color:var(--white);font-weight:500;white-space:nowrap}
.nav-btn{left:884px;top:0;width:213px;height:38px}
.hero-title{position:absolute;left:100px;top:225px;color:var(--white);font-size:44px;line-height:45px}
.hero-lead{position:absolute;left:100px;top:326px;color:var(--white);font-size:14px;line-height:22px;width:400px}
.hero-btn{left:101px;top:390px;width:143px;height:40px}
.dots{position:absolute;left:560px;top:582px;display:flex;gap:14px}
.dots i{width:10px;height:10px;border-radius:50%;background:rgba(255,255,255,.5)}
.dots i.on{background:var(--white)}

/* about */
.about{top:722px;height:511px}
.frame-back{position:absolute;background:var(--teal)}
.about h2,.insurance h2{font-size:46px;line-height:48px}

/* offer */
.offer{top:1233px;height:667px;background:linear-gradient(120deg,#2a8a80,#1f7f75 50%,#26867c)}
.offer h2{position:absolute;top:58px;width:100%;text-align:center;color:var(--white);font-size:46px}
.tab{position:absolute;top:144px;height:40px;display:flex;align-items:center;justify-content:center;font-size:17px;font-weight:500;color:var(--white)}
.tab.active{left:411px;width:179px;background:var(--ink)}
.tab.ghost{left:605px;width:186px;border:2px solid var(--white)}
.card{position:absolute;top:215px;width:316px;height:382px;background:var(--white);text-align:center}
.card .photo{left:7px;top:7px;width:302px;height:206px}
.card h3{position:absolute;top:226px;width:100%;font-size:22px;font-weight:600}
.card p{position:absolute;top:262px;left:20px;width:276px;font-size:14px;line-height:27px;color:var(--text)}
.card .btn{left:87px;top:328px;width:142px;height:38px}

/* insurance */
.insurance{top:1900px;height:515px}

/* testimonials */
.testi{top:2415px;height:594px;background:var(--teal-light)}
.sec-title{position:absolute;width:100%;text-align:center;font-size:46px}
.rule{position:absolute;left:565px;width:72px;height:3px;background:var(--teal)}
.quote{position:absolute;top:186px;width:484px;height:237px;background:var(--white);border-top:4px solid var(--teal);border-radius:8px}
.quote:after{content:"";position:absolute;left:224px;bottom:-18px;border-left:18px solid transparent;border-right:18px solid transparent;border-top:18px solid var(--white)}
.quote p{position:absolute;top:66px;left:24px;width:436px;text-align:center;font-style:italic;font-size:16px;line-height:34px;color:#333}
.quote .mark{position:absolute;right:20px;bottom:-4px;font-family:Georgia,serif;font-size:90px;line-height:90px;color:#ddd}
.avatar{position:absolute;top:-42px;left:195px;width:94px;height:94px;border-radius:50%;background:linear-gradient(160deg,#c9d7da,#8aa3a8);border:4px solid var(--white)}
.name{position:absolute;top:450px;width:484px;text-align:center;font-size:17px;font-weight:500}
.stars{position:absolute;top:476px;width:484px;text-align:center;color:var(--star);font-size:18px;letter-spacing:1px}
.arrow{position:absolute;top:282px}
.pager{position:absolute;top:518px;left:538px;display:flex;gap:12px}
.pager i{width:34px;height:2px;background:#8fc7c2}
.pager i.on{background:var(--teal);height:3px}

/* news */
.news{top:3009px;height:596px}
.post{position:absolute;top:155px;width:316px;height:362px}
.post .photo{left:0;top:0;width:316px;height:220px}
.post .date{position:absolute;right:16px;top:8px;width:52px;height:52px;border-radius:50%;background:var(--teal);color:var(--white);font-size:12px;font-weight:600;line-height:14px;text-align:center;padding-top:11px}
.post .box{position:absolute;left:11px;top:175px;width:294px;height:186px;background:var(--white);box-shadow:0 2px 10px rgba(0,0,0,.08);text-align:center}
.post .meta{margin-top:14px;font-size:11px;color:#555;display:flex;justify-content:center;gap:16px}
.post .meta b{color:var(--teal);font-weight:400}
.post h3{margin-top:10px;font-size:15px;font-weight:600;line-height:23px}
.post p{margin:6px 14px 0;font-size:13px;line-height:28px;color:var(--text)}

/* faq */
.faq{top:3605px;height:447px;background:var(--teal-light)}
.q{position:absolute;width:458px;height:40px;background:var(--white);border:1px solid #cfdede;display:flex;align-items:center;justify-content:space-between;padding:0 14px;font-size:14px;font-weight:600;white-space:nowrap}
.q span{font-size:24px;font-weight:300}

/* cta */
.cta{top:4052px;height:313px;background:linear-gradient(120deg,#1d7a70,#23877c)}
.cta h2{position:absolute;top:56px;width:100%;text-align:center;color:var(--white);font-size:46px}
.cta p{position:absolute;top:140px;width:100%;text-align:center;color:var(--white);font-size:14px;line-height:27px}
.cta-btn{left:493px;top:208px;width:213px;height:38px;background:var(--ink)}

/* footer */
.footer{top:4365px;height:286px;background:var(--footer);color:var(--white)}
.footer .logo{left:141px;top:60px;font-size:28px}
.social{position:absolute;left:102px;top:104px;display:flex;gap:10px}
.social i{width:34px;height:34px;border-radius:50%;border:2px solid var(--white)}
.fcol{position:absolute;top:57px}
.fcol h4{font-size:17px;font-weight:600;margin-bottom:12px;white-space:nowrap}
.fcol p,.fcol li{font-size:12px;line-height:16px;color:#ddd;list-style:none}
.fcol li{line-height:24px}
.fcol .row{display:flex;gap:8px;align-items:flex-start;margin-bottom:18px}
.email{position:absolute;left:803px;top:147px;width:294px;height:34px;border:1px solid #555;font-size:12px;color:#ccc;padding:9px 14px}
.email i{position:absolute;right:0;top:0;width:36px;height:32px;background:var(--teal);display:flex;align-items:center;justify-content:center}
.footer hr{position:absolute;left:99px;top:219px;width:1000px;border:0;border-top:1px solid #444}
.copy{position:absolute;top:250px;width:100%;text-align:center;font-size:12px;color:#ddd}
</style>
</head>
<body>

<header class="topbar">
  <span><svg width="14" height="14" viewBox="0 0 24 24" fill="none" stroke="#2fbfa8" stroke-width="2"><path d="M5 3h4l2 5-3 2a11 11 0 0 0 6 6l2-3 5 2v4a2 2 0 0 1-2 2A18 18 0 0 1 3 5a2 2 0 0 1 2-2z"/></svg>Hotline: +1 (888) 888-888</span>
  <span><svg width="13" height="15" viewBox="0 0 24 28" fill="none" stroke="#2fbfa8" stroke-width="2"><path d="M12 26s9-9 9-15a9 9 0 0 0-18 0c0 6 9 15 9 15z"/><circle cx="12" cy="11" r="3"/></svg>1234 Main Rd Somewhere, US 12345</span>
  <span><svg width="14" height="14" viewBox="0 0 24 24" fill="none" stroke="#2fbfa8" stroke-width="2"><circle cx="12" cy="12" r="10"/><path d="M12 6v6l4 2"/></svg>Mon-Sat: 8:00AM - 7:00PM</span>
</header>

<section class="hero">
  <div class="hero-photo" role="img" aria-label="Radiology staff preparing a patient lying on the table of an MRI scanner"></div>
  <div class="hero-shade"></div>
  <svg class="hero-curve" width="1200" height="686" viewBox="0 0 1200 686">
    <polygon points="0,578 820,676 1200,604 1200,686 0,686" fill="#ffffff"/>
    <polygon points="560,686 1200,584 1200,604 820,676" fill="#1f7f75"/>
  </svg>
  <nav class="nav">
    <div class="logo">LOGO</div>
    <div class="menu"><span>SERVICES</span><span>ABOUT US</span><span>PATIENT RESOURCES</span><span>CONTACT</span></div>
    <div class="btn nav-btn">Book an Appointment</div>
  </nav>
  <h1 class="hero-title slab">DIAGNOSTIC MRI<br>IMAGING CENTER</h1>
  <p class="hero-lead">Lorem ipsum dolor sit amet, consectetur adipiscing elit,<br>sed do eiusmod tempor incididunt</p>
  <div class="btn hero-btn">Get Started</div>
  <div class="dots"><i></i><i class="on"></i><i></i><i></i></div>
</section>

<section class="about">
  <div class="frame-back" style="left:99px;top:67px;width:452px;height:363px"></div>
  <div class="photo" style="left:112px;top:56px;width:453px;height:363px;background:linear-gradient(135deg,#d7e2e6,#7f98a2 60%,#3f5962)" role="img" aria-label="Clinicians reviewing MRI brain scans on monitors"></div>
  <h2 class="slab abs" style="left:641px;top:94px">ABOUT <span class="teal">US</span></h2>
  <p class="body abs" style="left:641px;top:163px;width:460px">Lorem ipsum dolor sit amet, consectetur adipiscing elit, sed do eiusmod tempor incididunt ut labore et dolore magna aliqua. Quis ipsum suspendisse ultrices gravida. Risus commodo viverra maecenas accumsan lacus vel facilisis.</p>
  <p class="body abs" style="left:641px;top:284px;width:460px">Lorem ipsum dolor sit amet, consectetur adipiscing elit, sed do eiusmod tempor incididunt ut labore et dolore</p>
  <div class="btn" style="left:644px;top:347px;width:143px;height:39px">Learn More</div>
</section>

<section class="offer">
  <h2 class="slab">WHAT WE OFFER</h2>
  <div class="tab active">MRI SERVICES</div>
  <div class="tab ghost">SPECIALIZATIONS</div>
  <div class="card" style="left:99px">
    <div class="photo" style="background:linear-gradient(135deg,#5a2a2a,#c23a3a 50%,#2a2a2a)" role="img" aria-label="Patient entering an MRI scanner for a brain scan"></div>
    <h3>BRAIN SCANS</h3>
    <p>Lorem ipsum dolor sit amet, consectetur adipiscing elit, sed do eiusmod</p>
    <div class="btn">Learn More</div>
  </div>
  <div class="card" style="left:442px">
    <div class="photo" style="background:linear-gradient(135deg,#c8d3ef,#5a74d8 55%,#2c3f9a)" role="img" aria-label="Patient positioned in an MRI scanner for a spine scan"></div>
    <h3>SPINE SCANS</h3>
    <p>Lorem ipsum dolor sit amet, consectetur adipiscing elit, sed do eiusmod</p>
    <div class="btn">Learn More</div>
  </div>
  <div class="card" style="left:783px">
    <div class="photo" style="background:linear-gradient(135deg,#e9e2dc,#c79a84 55%,#a33a34)" role="img" aria-label="Examination of a patient's arm for a musculoskeletal scan"></div>
    <h3>MUSCULOSKELETAL</h3>
    <p>Lorem ipsum dolor sit amet, consectetur adipiscing elit, sed do eiusmod</p>
    <div class="btn">Learn More</div>
  </div>
</section>

<section class="insurance">
  <h2 class="slab abs" style="left:99px;top:107px">INSURANCE <span class="teal">AND<br>BILLING</span></h2>
  <p class="body abs" style="left:99px;top:224px;width:460px">Lorem ipsum dolor sit amet, consectetur adipiscing elit, sed do eiusmod tempor incididunt ut labore et dolore magna aliqua. Quis ipsum suspendisse ultrices gravida. Risus commodo viverra maecenas accumsan lacus vel facilisis.</p>
  <div class="btn" style="left:103px;top:355px;width:143px;height:39px">Learn More</div>
  <div class="frame-back" style="left:646px;top:82px;width:453px;height:364px"></div>
  <div class="photo" style="left:634px;top:71px;width:454px;height:363px;background:linear-gradient(135deg,#b58f6a,#e7dccd 45%,#f4f2ee)" role="img" aria-label="Hands filling in insurance and billing forms next to a laptop"></div>
</section>

<section class="testi">
  <h2 class="sec-title slab" style="top:62px">TESTIMONIALS</h2>
  <div class="rule" style="top:121px"></div>
  <svg class="arrow" style="left:62px" width="20" height="36" viewBox="0 0 20 36" fill="none" stroke="#333" stroke-width="2"><path d="M18 2L2 18l16 16"/></svg>
  <svg class="arrow" style="left:1120px" width="20" height="36" viewBox="0 0 20 36" fill="none" stroke="#333" stroke-width="2"><path d="M2 2l16 16L2 34"/></svg>
  <div class="abs" style="left:101px;top:0;width:484px;height:594px">
    <div class="quote">
      <div class="avatar" role="img" aria-label="Portrait of a patient"></div>
      <p>Lorem ipsum dolor sit amet, consectetur adipiscing elit, sed do eiusmod tempor incididunt ut labore et dolore magna aliqua. Quis ium suspendisse ultrices gravida. Risus commodo viverra</p>
      <div class="mark">&rdquo;</div>
    </div>
    <div class="name">John Smith</div>
    <div class="stars">★★★★★</div>
  </div>
  <div class="abs" style="left:617px;top:0;width:484px;height:594px">
    <div class="quote">
      <div class="avatar" role="img" aria-label="Portrait of a patient"></div>
      <p>Lorem ipsum dolor sit amet, consectetur adipiscing elit, sed do eiusmod tempor incididunt ut labore et dolore magna aliqua. Quis ium suspendisse ultrices gravida. Risus commodo viverra</p>
      <div class="mark">&rdquo;</div>
    </div>
    <div class="name">John Smith</div>
    <div class="stars">★★★★★</div>
  </div>
  <div class="pager"><i></i><i class="on"></i><i></i></div>
</section>

<section class="news">
  <h2 class="sec-title slab" style="top:64px">LATEST <span class="teal">NEWS</span></h2>
  <div class="rule" style="top:122px"></div>
  <article class="post" style="left:99px">
    <div class="photo" style="background:linear-gradient(135deg,#0e2a4a,#2b6ea8 55%,#cfe0ee)" role="img" aria-label="Doctor pointing at MRI brain images on a screen"></div>
    <div class="date">JAN<br>2023</div>
    <div class="box">
      <div class="meta"><span><b>◌</b> 2 Comments</span><span><b>◌</b> By Admin</span></div>
      <h3>THE STANDARD LOREM IPSSAG<br>USED SINCE THE 1500S</h3>
      <p>Lorem ipsum dolor sit at, consectdetur adipiscing elit, sed do eiusmod tempor incididunt ut labore et dolore</p>
    </div>
  </article>
  <article class="post" style="left:442px">
    <div class="photo" style="background:linear-gradient(135deg,#e6e9ee,#7b8da6 55%,#2d3b55)" role="img" aria-label="Radiologist studying scan results on monitors"></div>
    <div class="date">JAN<br>2023</div>
    <div class="box">
      <div class="meta"><span><b>◌</b> 2 Comments</span><span><b>◌</b> By Admin</span></div>
      <h3>THE STANDARD LOREM IPSSAG<br>USED SINCE THE 1500S</h3>
      <p>Lorem ipsum dolor sit at, consectdetur adipiscing elit, sed do eiusmod tempor incididunt ut labore et dolore</p>
    </div>
  </article>
  <article class="post" style="left:785px">
    <div class="photo" style="background:linear-gradient(135deg,#0a1a3a,#1d4fbf 55%,#6fb0ff)" role="img" aria-label="MRI scanner room lit in blue"></div>
    <div class="date">JAN<br>2023</div>
    <div class="box">
      <div class="meta"><span><b>◌</b> 2 Comments</span><span><b>◌</b> By Admin</span></div>
      <h3>THE STANDARD LOREM IPSSAG<br>USED SINCE THE 1500S</h3>
      <p>Lorem ipsum dolor sit at, consectdetur adipiscing elit, sed do eiusmod tempor incididunt ut labore et dolore</p>
    </div>
  </article>
</section>

<section class="faq">
  <h2 class="sec-title slab" style="top:52px">FREQUENTLY ASKED QUESTION</h2>
  <div class="rule" style="top:112px"></div>
  <div class="q" style="left:130px;top:146px">The standard Lorem Ipssag used Finibus Bonorum<span>+</span></div>
  <div class="q" style="left:610px;top:146px">The standard Lorem Ipssag used Finibus Bonorum<span>+</span></div>
  <div class="q" style="left:130px;top:211px">The standard Lorem Ipssag used Finibus Bonorum<span>+</span></div>
  <div class="q" style="left:610px;top:211px">The standard Lorem Ipssag used Finibus Bonorum<span>+</span></div>
  <div class="q" style="left:130px;top:276px">The standard Lorem Ipssag used Finibus Bonorum<span>+</span></div>
  <div class="q" style="left:610px;top:276px">The standard Lorem Ipssag used Finibus Bonorum<span>+</span></div>
  <div class="q" style="left:130px;top:342px">The standard Lorem Ipssag used Finibus Bonorum<span>+</span></div>
  <div class="q" style="left:610px;top:342px">The standard Lorem Ipssag used Finibus Bonorum<span>+</span></div>
</section>

<section class="cta">
  <h2 class="slab">FINIBUS BONORUM ET</h2>
  <p>Lorem ipsum dolor sit amet, consectetur adipiscing elit, sed do eiusmod tempor incididunt ut labore<br>et dolore magna aliqua. Quis ipsum suspendisse ultrices gravida. Risus co maecenas</p>
  <div class="btn cta-btn">Book an Appointment</div>
</section>

<footer class="footer">
  <div class="logo">LOGO</div>
  <div class="social"><i></i><i></i><i></i><i></i></div>
  <div class="fcol" style="left:402px">
    <h4>CONTACT US</h4>
    <div class="row"><svg width="10" height="12" viewBox="0 0 24 28" fill="#fff"><path d="M12 26s9-9 9-15a9 9 0 0 0-18 0c0 6 9 15 9 15z"/></svg><p>1234 Main Rd<br>Somewhere, US 12345</p></div>
    <div class="row"><svg width="11" height="11" viewBox="0 0 24 24" fill="#fff"><path d="M5 3h4l2 5-3 2a11 11 0 0 0 6 6l2-3 5 2v4a2 2 0 0 1-2 2A18 18 0 0 1 3 5a2 2 0 0 1 2-2z"/></svg><p>+1 888-888-8888</p></div>
    <div class="row"><svg width="12" height="10" viewBox="0 0 24 18" fill="#fff"><path d="M0 0h24v18H0z"/><path d="M0 0l12 9 12-9" stroke="#171717" stroke-width="2" fill="none"/></svg><p>info@company.com</p></div>
  </div>
  <div class="fcol" style="left:630px">
    <h4>QUICK LINKS</h4>
    <ul><li>Home</li><li>Services</li><li>About Us</li><li>Patient Resources</li><li>Contact</li></ul>
  </div>
  <div class="fcol" style="left:803px">
    <h4>SIGN FOR NEWSLATTER</h4>
    <p style="line-height:22px">Stay connected on new products, events and<br>offers. Valid for new email subscribers only.</p>
  </div>
  <div class="email">Eamil<i><svg width="16" height="16" viewBox="0 0 24 24" fill="#fff"><path d="M2 12L22 3l-6 19-4-8z"/></svg></i></div>
  <hr>
  <div class="copy">Copyright ©2023 COMPANY. All Rights Reserved.</div>
</footer>

</body>
</html>
```